Dr. Pelham Billboard Sign Design

Family Dental Practice looking for a billboard sign design. We have Attached a Image of Dr Pelham and Her horse she would like to incorporate. The size of the sign is 118" tall and 196" Wide. We hired a previous designer to work on this also but would like to see what other come up with before we decide on a final. Please use something similar for a animal shelter icon to go beside the Animal Shelter Discount statement. You can use the text from the postcard file attached. I know text adjustments will be needed, but more interested in a eye catching design. Themes: Fall/Winter/Mountains/Nature , colors: open but Dr P like purple. We are open to ideas and will answer any questions.
TEXT
Theme: Fall/Winter/Mountain
Image: Dr Pelham with Horse (Same from mailer design)
Text to Keep that needs to be bold and Priority
1. Dr. Rosalind Pelham Family Dentistry
314 Brellin Court Spruce Pine, NC 28094
828-413-5276 | RPelhamDDS@Velmorx.net
(FaceBook icon) RosalindPelhamDDS
2. ACCEPTING NEW PATIENTS
3. Affordable Dentistry for Your Whole Family
4. WE FILE YOUR INSURANCE CLAIMS
5. Discounts for Senior Citizens, Law Enforcement, First Responders, Military Personnel, State Employees and College Students
6. (Cool Animal Shelter Icon) WE OFFER A DISCOUNT TO PATIENTS WHO SUPPORT OUR LOCAL ANIMAL SHELTERS BY ADOPTING, DONATING OR VOLUNTEERING
7. Schedule Your Appointment TODAY!
Target Market(s)
Local Community to Bring in Patients to dental office
Industry/Entity Type
Dental
Look and feel

```html
<!DOCTYPE html>
<html lang="en">
<head>
<meta charset="utf-8">
<title>Dr. Pelham Family Dentistry Billboard</title>
<link rel="stylesheet" href="https://fonts.googleapis.com/css2?family=Roboto+Condensed:wght@400;700;800&family=Roboto:wght@500;700&display=swap">
<style>
  :root {
    --page: #e4e4e4;
    --sky-top: #1d3fb8;
    --sky-mid: #2f7fe0;
    --sky-low: #8ec6f0;
    --ribbon: #92278f;
    --yellow: #e6ef1a;
    --navy: #2a1f6e;
    --white: #ffffff;
    --badge-dark: #0f2d7a;
    --badge-light: #2f78d6;
    --field: #a8287c;
  }
  html, body {
    margin: 0;
    padding: 0;
    width: 1200px;
    height: 1200px;
    overflow: hidden;
    background: var(--page);
  }
  .billboard {
    position: absolute;
    left: 20px;
    top: 252px;
    width: 1160px;
    height: 695px;
    box-shadow: 0 6px 24px rgba(0,0,0,0.18);
  }
  .condensed { font-family: "Roboto Condensed", "Arial Narrow", sans-serif; }
  .sans { font-family: "Roboto", Arial, sans-serif; }
</style>
</head>
<body>
<svg class="billboard" viewBox="0 0 1018 610" xmlns="http://www.w3.org/2000/svg">
  <defs>
    <linearGradient id="sky" x1="0" y1="0" x2="0" y2="1">
      <stop offset="0" stop-color="var(--sky-top)"/>
      <stop offset="0.3" stop-color="var(--sky-mid)"/>
      <stop offset="0.45" stop-color="var(--sky-low)"/>
      <stop offset="1" stop-color="var(--sky-low)"/>
    </linearGradient>
    <linearGradient id="landscape" x1="0" y1="0" x2="0" y2="1">
      <stop offset="0" stop-color="#b9d2e6"/>
      <stop offset="0.18" stop-color="#4f7a3a"/>
      <stop offset="0.35" stop-color="#6f8f58"/>
      <stop offset="0.45" stop-color="#a64a8f"/>
      <stop offset="1" stop-color="var(--field)"/>
    </linearGradient>
    <linearGradient id="portrait" x1="0" y1="0" x2="1" y2="1">
      <stop offset="0" stop-color="#4a2a1c"/>
      <stop offset="0.5" stop-color="#6e8a7a"/>
      <stop offset="1" stop-color="#d9a9c4"/>
    </linearGradient>
    <linearGradient id="band" x1="0" y1="0" x2="1" y2="0">
      <stop offset="0" stop-color="#1a2a8a" stop-opacity="0"/>
      <stop offset="0.12" stop-color="#1a2a8a" stop-opacity="0.9"/>
      <stop offset="0.88" stop-color="#1a2a8a" stop-opacity="0.9"/>
      <stop offset="1" stop-color="#1a2a8a" stop-opacity="0"/>
    </linearGradient>
    <radialGradient id="badge" cx="0.5" cy="0.3" r="0.75">
      <stop offset="0" stop-color="var(--badge-light)"/>
      <stop offset="1" stop-color="var(--badge-dark)"/>
    </radialGradient>
  </defs>

  <rect class="sky" x="0" y="0" width="1018" height="610" fill="url(#sky)"/>

  <g class="scenery" role="img" aria-label="Photo of a snow-capped mountain, evergreen forest, a lake and a field of pink-purple flowers">
    <rect x="0" y="255" width="1018" height="355" fill="url(#landscape)"/>
  </g>

  <g class="portrait" role="img" aria-label="Photo of Dr. Pelham standing beside her bay horse">
    <rect x="359" y="255" width="315" height="355" fill="url(#portrait)"/>
  </g>

  <g class="ribbon">
    <polygon points="27,0 186,0 186,238 106,178 27,238" fill="var(--ribbon)"/>
    <text class="condensed" x="106" y="48" font-size="28" font-weight="700" fill="var(--white)" text-anchor="middle">Schedule Your</text>
    <text class="condensed" x="106" y="82" font-size="28" font-weight="700" fill="var(--white)" text-anchor="middle">Appointment</text>
    <text class="condensed" x="106" y="138" font-size="44" font-weight="800" fill="var(--yellow)" text-anchor="middle">TODAY!</text>
  </g>

  <g class="masthead">
    <text class="condensed" x="502" y="88" font-size="72" font-weight="800" fill="var(--yellow)" text-anchor="middle" textLength="588" lengthAdjust="spacingAndGlyphs">Dr. Rosalind Pelham</text>
    <text class="sans" x="509" y="130" font-size="38" font-weight="700" fill="var(--navy)" text-anchor="middle">Family Dentistry</text>
    <text class="sans" x="509" y="164" font-size="21" font-weight="500" fill="var(--white)" text-anchor="middle">Affordable Dentistry for Your Whole Family</text>
  </g>

  <g class="discounts">
    <rect x="199" y="177" width="620" height="67" fill="url(#band)"/>
    <text class="condensed" x="509" y="204" font-size="23" font-weight="700" fill="var(--white)" text-anchor="middle">Discounts for Senior Citizens, Law Enforcement, First Responders,</text>
    <text class="condensed" x="509" y="233" font-size="23" font-weight="700" fill="var(--white)" text-anchor="middle">Military Personnel, State Employees and College Students</text>
  </g>

  <g class="shelter-mark" role="img" aria-label="Animal shelter icon with a dog and cat">
    <circle cx="912" cy="99" r="72" fill="var(--white)"/>
    <circle cx="912" cy="99" r="60" fill="#2a6ad0"/>
  </g>

  <g class="badge badge-patients">
    <circle cx="164" cy="394" r="87" fill="url(#badge)" stroke="#3f8fe6" stroke-width="3"/>
    <text class="sans" x="164" y="373" font-size="23" font-weight="700" fill="var(--white)" text-anchor="middle">ACCEPTING</text>
    <text class="sans" x="164" y="402" font-size="23" font-weight="700" fill="var(--white)" text-anchor="middle">NEW</text>
    <text class="sans" x="164" y="431" font-size="23" font-weight="700" fill="var(--white)" text-anchor="middle">PATIENTS</text>
  </g>

  <g class="badge badge-insurance">
    <circle cx="854" cy="394" r="87" fill="url(#badge)" stroke="#3f8fe6" stroke-width="3"/>
    <text class="sans" x="854" y="361" font-size="22" font-weight="700" fill="var(--white)" text-anchor="middle">WE FILE</text>
    <text class="sans" x="854" y="388" font-size="22" font-weight="700" fill="var(--white)" text-anchor="middle">YOUR</text>
    <text class="sans" x="854" y="415" font-size="22" font-weight="700" fill="var(--white)" text-anchor="middle">INSURANCE</text>
    <text class="sans" x="854" y="442" font-size="22" font-weight="700" fill="var(--white)" text-anchor="middle">CLAIMS</text>
  </g>

  <g class="contact-left">
    <text class="sans" x="164" y="527" font-size="34" font-weight="700" fill="var(--white)" text-anchor="middle">828-413-5276</text>
    <text class="sans" x="164" y="555" font-size="20" font-weight="500" fill="var(--yellow)" text-anchor="middle">314 Brellin Court Spruce</text>
    <text class="sans" x="164" y="582" font-size="20" font-weight="500" fill="var(--yellow)" text-anchor="middle">Pine, NC 28094</text>
  </g>

  <g class="contact-right">
    <rect x="680" y="520" width="28" height="28" rx="3" fill="#3b64c0"/>
    <text class="sans" x="716" y="542" font-size="24" font-weight="500" fill="var(--white)">RosalindPelhamDDS</text>
    <text class="sans" x="850" y="576" font-size="24" font-weight="500" fill="var(--yellow)" text-anchor="middle">RPelhamDDS@Velmorx.net</text>
  </g>
</svg>
</body>
</html>
```